Can you create a Business Card based on the Logo you designed.

See example and would like to see other examples.

Trying to keep it very clean with a focus on the logo and name.

```html
<!DOCTYPE html>
<html lang="en">
<head>
<meta charset="UTF-8">
<title>Fieldra Business Card</title>
<link href="https://fonts.googleapis.com/css2?family=Montserrat:wght@400;500;700;800&display=swap" rel="stylesheet">
<style>
  :root {
    --bg: #262626;
    --card-white: #ffffff;
    --green-deep: #0f6a2c;
    --green-mid: #1f7d36;
    --green-light: #4fa546;
    --sun: #f0a030;
    --ink: #222222;
  }
  * { margin: 0; padding: 0; box-sizing: border-box; }
  html, body {
    width: 1200px; height: 900px; overflow: hidden;
    background: var(--bg);
    font-family: "Montserrat", sans-serif;
  }
  .stage {
    position: relative; width: 1200px; height: 900px;
  }
  .card {
    position: absolute; left: 285px; width: 630px; height: 360px;
    border-radius: 22px; overflow: hidden;
  }
  .card-back { top: 50px; }
  .card-front { top: 490px; background: var(--card-white); }

  .back-pattern {
    position: absolute; inset: 0;
    background: linear-gradient(120deg, #4ea04a 0%, #2a8439 35%, #1d7332 65%, #3f9a42 100%);
  }
  .back-brand {
    position: absolute; left: 420px; top: 262px;
    display: flex; align-items: center; gap: 8px;
    color: var(--card-white); font-weight: 800; font-size: 22px;
  }
  .brand-dot {
    width: 14px; height: 14px; border-radius: 50%; background: var(--sun);
  }

  .front-brand {
    position: absolute; left: 40px; top: 48px;
    display: flex; align-items: center; gap: 12px;
    color: var(--green-mid); font-weight: 800; font-size: 54px; letter-spacing: 0.5px;
  }
  .front-brand .brand-dot { width: 26px; height: 26px; }

  .holder-name {
    position: absolute; left: 40px; top: 184px;
    color: var(--green-mid); font-weight: 800; font-size: 27px;
  }
  .holder-title {
    position: absolute; left: 40px; top: 222px;
    color: var(--ink); font-weight: 400; font-size: 16px;
  }
  .rule-long {
    position: absolute; left: 260px; right: 36px; top: 206px;
    height: 1.5px; background: var(--green-deep);
  }
  .rule-short {
    position: absolute; left: 40px; top: 254px;
    width: 210px; height: 1.5px; background: var(--green-deep);
  }
  .contact-list {
    position: absolute; left: 40px; top: 264px; list-style: none;
  }
  .contact-list li {
    display: flex; align-items: center; gap: 12px;
    font-size: 15px; color: var(--ink); height: 25px;
  }
  .contact-list svg { width: 14px; height: 14px; fill: var(--green-deep); }
  .address {
    position: absolute; right: 40px; top: 222px; text-align: right;
    font-size: 15px; color: var(--ink); line-height: 1.3;
  }
</style>
</head>
<body>
<main class="stage">
  <section class="card card-back">
    <div class="back-pattern" role="img" aria-label="Repeating leaf-and-sun pattern in shades of green"></div>
    <div class="back-brand"><span class="brand-dot"></span>Fieldra</div>
  </section>

  <section class="card card-front">
    <div class="front-brand"><span class="brand-dot"></span>Fieldra</div>

    <h1 class="holder-name">Marcus Hale</h1>
    <p class="holder-title">Chief Executive Officer</p>
    <div class="rule-long"></div>
    <div class="rule-short"></div>

    <ul class="contact-list">
      <li>
        <svg viewBox="0 0 16 16" aria-hidden="true"><path d="M3 1h3l1.5 4-2 1.2a9 9 0 0 0 4.3 4.3L11 8.5 15 10v3a2 2 0 0 1-2 2C6.4 15 1 9.6 1 3a2 2 0 0 1 2-2z"/></svg>
        +1 (614) 555-0182
      </li>
      <li>
        <svg viewBox="0 0 16 16" aria-hidden="true"><path d="M1 3h14v10H1z M1 3l7 6 7-6" fill="none" stroke="#0f6a2c" stroke-width="2"/></svg>
        ceo@fieldra.com
      </li>
      <li>
        <svg viewBox="0 0 16 16" aria-hidden="true"><circle cx="8" cy="8" r="6.5" fill="none" stroke="#0f6a2c" stroke-width="2"/><path d="M1.5 8h13M8 1.5c-3 3.5-3 9.5 0 13M8 1.5c3 3.5 3 9.5 0 13" fill="none" stroke="#0f6a2c" stroke-width="1.2"/></svg>
        www.fieldra.com
      </li>
    </ul>

    <address class="address" style="font-style:normal">
      418 Meadow Ridge Rd, #12<br>
      Dayton, OH 45402
    </address>
  </section>
</main>
</body>
</html>
```